Law Firm Logo and Business Card Design

I need a logo and business card design for a law firm I just started. The law firm is named Law Office of Doreen K. Ashworth, LLC. The type of law I practice is Family Law, which includes divorce, custody, child support, alimony, property division, and the like. I would like to see designs that are unique and modern, yet sophisticated. I would also like to use the logo/design for my letterhead. I am not opposed to using some form of the scales of justice although I'd like something other than the typical, old fashioned scales of justice. I had considered a house made out of puzzle pieces with one puzzle piece pulled away from the others, with the logo text reading "Putting your life back together, one piece at a time." However, I don't want that particular design to look juvenile. I also would not be opposed to some form of my initials on the logo -- my initials are DKA. I am open to any other ideas you may have. I would like to see raised designs/lettering, and/or metallic finish. I like the colors black, white, gold, silver, and/or teal.

Industry/Entity Type

Law Firm

```html
<!DOCTYPE html>
<html lang="en">
<head>
<meta charset="utf-8">
<title>Law Office of Doreen K. Ashworth, LLC — Business Card</title>
<link href="https://fonts.googleapis.com/css2?family=Carlito:wght@400;700&display=swap" rel="stylesheet">
<style>
  :root {
    --stage: #000000;
    --paper: #ffffff;
    --paper-shade: #e9e9eb;
    --deep-blue: #2a57a6;
    --mid-blue: #2e7fbf;
    --aqua: #3cbad2;
    --crescent-blue: #2a8fce;
    --rim-grey: #a9a9ab;
    --brand-blue: #1f6fb8;
    --ink-light: #ffffff;
  }
  html, body {
    margin: 0;
    padding: 0;
    width: 1200px;
    height: 999px;
    overflow: hidden;
    background: var(--stage);
  }
  .canvas {
    position: relative;
    width: 1200px;
    height: 999px;
    background: var(--stage);
    font-family: "Carlito", "Calibri", sans-serif;
  }
  .card {
    position: absolute;
    left: 75px;
    top: 199px;
    width: 1051px;
    height: 600px;
    overflow: hidden;
  }
  .card-art {
    position: absolute;
    inset: 0;
    display: block;
  }
  .brand {
    position: absolute;
    left: 0;
    top: 90px;
    width: 462px;
    text-align: center;
    color: var(--brand-blue);
    font-weight: 400;
  }
  .brand-mark {
    display: block;
    margin: 0 auto 18px;
    width: 132px;
    height: 132px;
    border-radius: 50%;
    border: 4px solid var(--brand-blue);
    box-sizing: border-box;
  }
  .brand-name {
    margin: 0;
    font-size: 36px;
    line-height: 38px;
    font-weight: 400;
  }
  .details {
    position: absolute;
    left: 547px;
    top: 100px;
    color: var(--ink-light);
  }
  .person-name {
    margin: 0;
    font-size: 44px;
    line-height: 50px;
    font-weight: 700;
  }
  .person-role {
    margin: 0;
    font-size: 29px;
    line-height: 34px;
  }
  .address {
    margin: 22px 0 0;
    font-size: 32px;
    line-height: 41px;
    font-style: normal;
  }
  .contact-list {
    list-style: none;
    margin: 30px 0 0;
    padding: 0;
    font-size: 32px;
    line-height: 41.5px;
  }
  .contact-list li {
    display: flex;
    align-items: center;
    gap: 12px;
  }
  .contact-icon {
    width: 30px;
    height: 30px;
    flex: none;
  }
</style>
</head>
<body>
<main class="canvas">
  <section class="card">
    <svg class="card-art" width="1051" height="600" viewBox="0 0 1051 600" aria-hidden="true">
      <defs>
        <radialGradient id="panelGlow" cx="1" cy="0.3" r="1.1">
          <stop offset="0" stop-color="var(--aqua)"/>
          <stop offset="0.45" stop-color="var(--mid-blue)"/>
          <stop offset="1" stop-color="var(--deep-blue)"/>
        </radialGradient>
        <linearGradient id="paperFade" x1="0" y1="0" x2="1" y2="0">
          <stop offset="0" stop-color="var(--paper-shade)"/>
          <stop offset="0.35" stop-color="var(--paper)"/>
          <stop offset="1" stop-color="var(--paper)"/>
        </linearGradient>
      </defs>
      <rect class="blue-panel" width="1051" height="600" fill="url(#panelGlow)"/>
      <path class="rim" fill="var(--rim-grey)"
        d="M0,0 L364,0 C452,52 499,180 494,300 C489,440 427,542 366,600 L0,600 Z"/>
      <path class="crescent" fill="var(--crescent-blue)"
        d="M0,0 L356,0 C444,52 491,180 486,300 C481,440 419,542 356,600 L0,600 Z"/>
      <path class="white-field" fill="url(#paperFade)"
        d="M0,0 L356,0 C444,52 491,180 486,271 C478,420 370,540 255,600 L0,600 Z"/>
    </svg>

    <div class="brand">
      <span class="brand-mark"></span>
      <p class="brand-name">Law Office of Doreen K.<br>Ashworth, LLC</p>
    </div>

    <div class="details">
      <h1 class="person-name">Title name</h1>
      <p class="person-role">designation</p>
      <address class="address">Add:&nbsp; Lorem ipsum dolor sit<br>amet, consectetur adipiscing<br>elit,Lorem ipsum dolor</address>
      <ul class="contact-list">
        <li>
          <svg class="contact-icon" viewBox="0 0 30 30" aria-label="Mobile">
            <rect x="2" y="1" width="26" height="28" rx="5" fill="#fff"/>
            <rect x="8" y="5" width="14" height="17" rx="1.5" fill="var(--mid-blue)"/>
            <circle cx="15" cy="25" r="1.6" fill="var(--mid-blue)"/>
          </svg>
          <span>000-000-0000</span>
        </li>
        <li>
          <svg class="contact-icon" viewBox="0 0 30 30" aria-label="Fax">
            <rect x="8" y="1" width="14" height="11" fill="#fff"/>
            <rect x="2" y="13" width="26" height="16" rx="3" fill="#fff"/>
            <rect x="8" y="19" width="14" height="4" rx="2" fill="var(--mid-blue)"/>
          </svg>
          <span>000-000-0000</span>
        </li>
        <li>
          <svg class="contact-icon" viewBox="0 0 30 30" aria-label="Email">
            <path d="M2,12 L15,2 L28,12 L28,28 L2,28 Z" fill="#fff"/>
            <path d="M2,12 L15,21 L28,12" fill="none" stroke="var(--mid-blue)" stroke-width="2.5"/>
          </svg>
          <span>abcd@ashworthmail.com</span>
        </li>
        <li>
          <svg class="contact-icon" viewBox="0 0 30 30" aria-label="Website">
            <rect x="1" y="1" width="28" height="28" rx="6" fill="#fff"/>
            <text x="15" y="22" text-anchor="middle" font-family="Carlito, sans-serif" font-size="22" font-weight="700" fill="var(--mid-blue)">@</text>
          </svg>
          <span>www.dkalawoffice.com</span>
        </li>
      </ul>
    </div>
  </section>
</main>
</body>
</html>
```